Town Wordpress Design Project

Hi,
I am looking for someone to completely start from scratch on a website for a town in Texas named Lakeside. I designed their last website about 4 years ago but am not able to give them what I would like to with my abilities. I need a wordpress website that is web 2.0 in design while still being creative. Their current website can be seen at www.brindowvale.us. They like such websites by a company named Marvenlo, you can view their town website portfolio here: http://www.marvenlo.com/index.aspx?NID=137. I would need all of the pages and info that is on their current site to be moved to the new site that I am hoping you can create for me. I want a much cleaner, nicer, and simpler navigation panel, while hiding links in drop down menus. I also want to include a calendar where they could post upcoming events and would want them to be able to add submit-able forms whenever they would need to. A search option would also be nice. I know that this is a design community, but if you could code the site as well or know someone who can, please let me know. Their Town Logo can be found attached, and the font in which you spell out their town name is totally up to you. They want their Agenda and Minutes to display like this: http://www.qwobel.com/index.aspx?NID=266. Let me know if you have any further questions...
If at all possible, I wouldn't mind the design to be designed in such a way that making it "responsive" someday would be easily possible...
Reason: More time needed for some designers...
Reason: Additional time needed...

```html
<!DOCTYPE html>
<html lang="en">
<head>
<meta charset="utf-8">
<title>Town of Brindowvale</title>
<link href="https://fonts.googleapis.com/css2?family=Arimo:wght@400;700&family=Tinos&display=swap" rel="stylesheet">
<style>
  :root {
    --page: #f4f4f4;
    --navy: #0b2d6b;
    --navy-dark: #082468;
    --nav-top: #2f63c4;
    --nav-bottom: #0a2a78;
    --red: #c10a31;
    --text: #222;
    --muted: #555;
    --rule: #c8c8c8;
    --white: #fff;
  }
  * { box-sizing: border-box; margin: 0; padding: 0; }
  html, body { width: 1200px; height: 869px; overflow: hidden; }
  body { background: var(--page); font-family: "Arimo", Arial, sans-serif; color: var(--text); position: relative; }
  a { color: inherit; text-decoration: none; }

  .brand { position: absolute; left: 120px; top: 8px; display: flex; align-items: center; gap: 22px; }
  .brand-mark { width: 150px; height: 150px; border-radius: 50%; background: var(--navy); }
  .brand-name { font-family: "Tinos", "Times New Roman", serif; color: var(--navy); font-size: 48px; line-height: 58px; letter-spacing: 1px; font-weight: 400; }

  .utility { position: absolute; right: 120px; top: 14px; font-size: 12px; color: #222; }
  .utility a + a::before { content: "|"; margin: 0 6px; }

  .contact { position: absolute; left: 790px; top: 68px; }
  .contact address { font-style: normal; font-size: 18px; line-height: 18px; letter-spacing: 1px; color: #111; }
  .contact .phone { display: block; margin-top: 8px; font-size: 32px; color: var(--red); letter-spacing: 0.5px; }

  .main-nav { position: absolute; left: 120px; top: 175px; width: 960px; height: 38px; border-radius: 4px;
    background: linear-gradient(var(--nav-top), var(--nav-bottom)); display: flex; justify-content: space-between; align-items: center; padding: 0 28px; }
  .main-nav a { color: var(--white); font-size: 17px; }

  .hero { position: absolute; left: 120px; top: 231px; width: 671px; height: 260px; border-radius: 5px;
    background: linear-gradient(180deg, #a89d8a 0%, #8e8779 45%, #9a7a66 100%); }

  .panel { position: absolute; left: 819px; width: 261px; border: 2px solid var(--red); border-radius: 5px; background: var(--white); overflow: hidden; }
  .panel h2 { background: var(--red); color: var(--white); font-size: 18px; font-weight: 400; height: 33px; line-height: 33px; padding-left: 12px; }
  .news { top: 233px; height: 258px; }
  .news-item { margin: 0 10px; padding: 12px 2px 8px; border-bottom: 2px dotted #888; }
  .news-item p { font-size: 13.5px; line-height: 17px; text-align: justify; color: #222; }
  .more { display: flex; justify-content: flex-end; align-items: center; gap: 6px; font-size: 12px; margin-top: 8px; color: var(--navy); }
  .more svg { width: 7px; height: 10px; }
  .news .more.all { margin: 6px 10px 0; }
  .events { top: 521px; height: 257px; }
  .events ul { list-style: none; padding: 12px 12px 0; }
  .events li { margin-bottom: 14px; font-size: 14px; line-height: 18px; }
  .events time { display: block; color: var(--navy); }

  .feature { position: absolute; top: 518px; width: 210px; }
  .feature h2 { font-size: 18px; font-weight: 400; color: var(--navy); height: 31px; }
  .feature .thumb { height: 93px; border-radius: 5px; }
  .feature p { margin-top: 15px; font-size: 12px; line-height: 14.5px; color: var(--muted); text-align: justify; }
  .feature .more { color: var(--red); margin-top: 15px; }
  .thumb-dishes { background: linear-gradient(180deg, #3f7fc6, #b7c9dc); }
  .thumb-keyboard { background: linear-gradient(135deg, #d7dde6, #6c7a8c 60%, #1f252c); }
  .thumb-waterpark { background: linear-gradient(180deg, #4f8a3c, #b84a7a 50%, #5ec4dd); }

  .site-footer { position: absolute; left: 120px; top: 805px; width: 960px; border-top: 1px solid var(--rule); padding-top: 13px;
    font-size: 12px; line-height: 14px; text-align: center; color: #222; }
</style>
</head>
<body>
  <header>
    <div class="brand">
      <span class="brand-mark" aria-hidden="true"></span>
      <div class="brand-name">TOWN OF<br>BRINDOWVALE</div>
    </div>
    <nav class="utility">
      <a href="#">News &amp; Events</a><a href="#">City Council</a><a href="#">Police</a><a href="#">FAQ's</a><a href="#">Contact Us</a>
    </nav>
    <div class="contact">
      <address>4120 HARLOW CREEK RD.<br>BRINDOWVALE, TX 76000</address>
      <span class="phone">555-318-4072</span>
    </div>
  </header>

  <nav class="main-nav">
    <a href="#">Home</a><a href="#">Our Community</a><a href="#">Recreation</a><a href="#">Departments</a><a href="#">Services</a><a href="#">Online Payments</a><a href="#">How Do I?</a>
  </nav>

  <div class="hero" role="img" aria-label="Police car parked beside the brick town hall sign"></div>

  <section class="panel news">
    <h2>Latest News</h2>
    <div class="news-item">
      <p>Lorem ipsum dolor sit amet, ki sfsi ip consectetur adipiscing elit. Fusce tincidunt dignissim euismod.</p>
      <a class="more" href="#"><svg viewBox="0 0 7 10"><path d="M1 1l4 4-4 4" fill="none" stroke="currentColor" stroke-width="2"/></svg>Read More</a>
    </div>
    <div class="news-item">
      <p>Lorem ipsum dolor sit amet, ki sfsi ip consectetur adipiscing elit. Fusce tincidunt dignissim euismod.</p>
      <a class="more" href="#"><svg viewBox="0 0 7 10"><path d="M1 1l4 4-4 4" fill="none" stroke="currentColor" stroke-width="2"/></svg>Read More</a>
    </div>
    <a class="more all" href="#"><svg viewBox="0 0 7 10"><path d="M1 1l4 4-4 4" fill="none" stroke="currentColor" stroke-width="2"/></svg>View All</a>
  </section>

  <section class="panel events">
    <h2>Upcomming Events</h2>
    <ul>
      <li><time>September 26, 2012</time>Lorem ipsum dolor</li>
      <li><time>September 28, 2012</time>Lorem ipsum dolor</li>
      <li><time>September 30, 2012</time>Lorem ipsum dolor</li>
      <li><time>October 2, 2012</time>Lorem ipsum dolor</li>
    </ul>
  </section>

  <section class="feature" style="left:120px">
    <h2>Facilities &amp; Services</h2>
    <div class="thumb thumb-dishes" role="img" aria-label="Satellite dishes under a blue sky"></div>
    <p>Lorem ipsum dolor sit amet, consectetur adipiscing elit. Fusce tincidunt dignissim euismod. Class aptent taciti sociosqu ad litora torquent per conubia nostra, per inceptos himenaeos.</p>
    <a class="more" href="#"><svg viewBox="0 0 7 10"><path d="M1 1l4 4-4 4" fill="none" stroke="currentColor" stroke-width="2"/></svg>Read More</a>
  </section>
  <section class="feature" style="left:351px">
    <h2>Online Payments</h2>
    <div class="thumb thumb-keyboard" role="img" aria-label="Hands typing on a laptop keyboard"></div>
    <p>Lorem ipsum dolor sit amet, consectetur adipiscing elit. Fusce tincidunt dignissim euismod. Class aptent taciti sociosqu ad litora torquent per conubia nostra, per inceptos himenaeos.</p>
    <a class="more" href="#"><svg viewBox="0 0 7 10"><path d="M1 1l4 4-4 4" fill="none" stroke="currentColor" stroke-width="2"/></svg>Read More</a>
  </section>
  <section class="feature" style="left:582px">
    <h2>Featured Projects</h2>
    <div class="thumb thumb-waterpark" role="img" aria-label="Water park slides above a pool"></div>
    <p>Lorem ipsum dolor sit amet, consectetur adipiscing elit. Fusce tincidunt dignissim euismod. Class aptent taciti sociosqu ad litora torquent per conubia nostra, per inceptos himenaeos.</p>
    <a class="more" href="#"><svg viewBox="0 0 7 10"><path d="M1 1l4 4-4 4" fill="none" stroke="currentColor" stroke-width="2"/></svg>Read More</a>
  </section>

  <footer class="site-footer">
    © 2007-2010 Town of Brindowvale, Texas. Every effort is made to ensure the information provided on these pages is timely and correct. However, users should keep in mind that this information is provided only as a public convenience. In any case where legal reliance on information is required, contact the Town of Brindowvale at 555-318-4072, ext. 303 to request a copy of the official records
  </footer>
</body>
</html>
```